Attic Rescue Belle - Word Press

I have a logo, and would like a design template for a wordpress blog incorporating the look / feel of the logo.

It is really a rather basic blog: want to be able to blog and post photos. Nothing unusual involved in content - just want a customized look for the overall blog.

logo attached.

ARB is a blog addressing issues of interior design, salvage, and general self help (esteem building). It is eclectic and fun in it's approach - but is serious about providing good content.

Thanks!

```html
<!DOCTYPE html>
<html lang="en">
<head>
<meta charset="utf-8">
<title>Attic Rescue Belle</title>
<link rel="stylesheet" href="https://fonts.googleapis.com/css2?family=Open+Sans:wght@400;600;700&display=swap">
<style>
:root{
  --page-bg:#eeeedf;
  --panel:#ffffff;
  --pink:#e0509a;
  --pink-dark:#d8418b;
  --pink-text:#e0357f;
  --red-btn:#ea3340;
  --title:#3a3a3a;
  --body:#5a5a5a;
  --list:#444444;
  --rule:#dddddd;
}
*{box-sizing:border-box;margin:0;padding:0}
html,body{width:1035px;height:1200px;overflow:hidden;background:var(--page-bg)}
body{font-family:"Open Sans",Verdana,sans-serif}
.stage{position:relative;width:1200px;height:1391px;transform:scale(.8625);transform-origin:0 0}
.abs{position:absolute}
.nav{left:120px;top:31px;width:960px;height:47px;background:linear-gradient(#ea5aa2,var(--pink-dark));border-radius:2px}
.nav a{position:absolute;top:15px;color:#fff;font-size:15px;text-decoration:none;letter-spacing:.2px}
.panel{left:120px;top:90px;width:960px;height:1240px;background:var(--panel)}
.hero{left:127px;top:95px;width:662px;height:272px;background:linear-gradient(100deg,#a9bccc 0%,#5a6576 35%,#9aaabd 60%,#e9dccc 80%,#c7d2dc 100%)}
.logo-box{left:802px;top:96px;width:272px;height:271px;border:2px solid var(--pink);background:var(--page-bg);display:flex;align-items:center;justify-content:center}
.logo-name{font-size:22px;font-weight:600;color:#555;display:flex;align-items:center;gap:10px}
.logo-name i{display:block;width:18px;height:18px;border-radius:50%;background:var(--pink)}
.social{left:812px;top:379px;display:flex;gap:11px}
.social span{width:26px;height:26px;border-radius:50%;background:#b9c4cc}
.feed-box{left:804px;width:269px;height:50px;border:1px solid var(--rule);display:flex;align-items:center;padding-left:12px;gap:8px;font-size:11px;font-weight:700;color:#333;letter-spacing:-.3px}
.feed-dot{flex:none;width:26px;height:26px;border-radius:50%}
.side-head{left:802px;width:272px;height:38px;background:linear-gradient(#ea5aa2,var(--pink-dark));color:#fff;font-size:17px;padding:6px 9px;border-radius:2px}
.side-list{left:810px;list-style:none}
.side-list li{display:flex;align-items:center;gap:11px;height:23.5px;font-size:15px;color:var(--list);letter-spacing:.2px}
.side-list li svg{flex:none}
.ad{left:804px;top:1092px;width:269px;height:217px;border:1px solid #ccc;background:linear-gradient(#ffffff 0%,#ffffff 44%,#2aa8ae 44%,#2aa8ae 100%)}
.post{left:133px;width:645px;height:200px}
.post h2{font-size:17px;font-weight:400;color:var(--title);letter-spacing:.2px}
.meta{display:flex;align-items:center;gap:6px;margin-top:6px;font-size:11px;color:var(--pink-text);letter-spacing:.4px}
.meta .sep{width:10px}
.thumb{position:absolute;left:-1px;top:54px;width:170px;height:143px}
.excerpt{position:absolute;left:181px;top:51px;width:460px;font-size:12px;line-height:18px;color:var(--body);letter-spacing:.1px}
.excerpt span{display:block;white-space:nowrap;text-align:justify;text-align-last:justify}
.excerpt span:last-child{text-align-last:left}
.more{position:absolute;left:180px;top:163px;width:92px;height:33px;background:var(--red-btn);color:#fff;font-size:15px;display:flex;align-items:center;justify-content:center;border-radius:2px}
.footer{left:0;width:1100px;top:1342px;text-align:center;font-size:11.5px;color:var(--pink-text);letter-spacing:.5px}
.footer b{font-weight:700;letter-spacing:1px}
</style>
</head>
<body>
<div class="stage">
  <nav class="abs nav">
    <a href="#" style="left:28px">HOME</a>
    <a href="#" style="left:112px">ABOUT US</a>
    <a href="#" style="left:234px">IMAGES</a>
    <a href="#" style="left:343px">CONTACT US</a>
  </nav>

  <div class="abs panel"></div>
  <div class="abs hero" role="img" aria-label="Photo of a smiling businesswoman in front of colleagues in an office"></div>

  <div class="abs logo-box"><div class="logo-name"><i></i>Attic Rescue Belle</div></div>
  <div class="abs social"><span></span><span></span><span></span><span></span><span></span><span></span><span></span></div>

  <div class="abs feed-box" style="top:427px"><span class="feed-dot" style="background:#e8602c"></span>SUBSCRIBE TO OUR RSS FEED!</div>
  <div class="abs feed-box" style="top:486px"><span class="feed-dot" style="background:#4aa9dc"></span>FOLLOW US ON CHIRPER!</div>

  <div class="abs side-head" style="top:550px">Category</div>
  <ul class="abs side-list" style="top:594px">
    <li><svg width="14" height="14" viewBox="0 0 14 14"><circle cx="7" cy="7" r="6" fill="none" stroke="#555" stroke-width="1.3"/><path d="M5.5 4l3.5 3-3.5 3z" fill="#555"/></svg>Interior Design</li>
    <li><svg width="14" height="14" viewBox="0 0 14 14"><circle cx="7" cy="7" r="6" fill="none" stroke="#555" stroke-width="1.3"/><path d="M5.5 4l3.5 3-3.5 3z" fill="#555"/></svg>Salvage</li>
    <li><svg width="14" height="14" viewBox="0 0 14 14"><circle cx="7" cy="7" r="6" fill="none" stroke="#555" stroke-width="1.3"/><path d="M5.5 4l3.5 3-3.5 3z" fill="#555"/></svg>General Self Help</li>
    <li><svg width="14" height="14" viewBox="0 0 14 14"><circle cx="7" cy="7" r="6" fill="none" stroke="#555" stroke-width="1.3"/><path d="M5.5 4l3.5 3-3.5 3z" fill="#555"/></svg>Serious Good Content</li>
    <li><svg width="14" height="14" viewBox="0 0 14 14"><circle cx="7" cy="7" r="6" fill="none" stroke="#555" stroke-width="1.3"/><path d="M5.5 4l3.5 3-3.5 3z" fill="#555"/></svg>Esteem Building</li>
  </ul>

  <div class="abs side-head" style="top:731px">Recent &nbsp;Posts</div>
  <ul class="abs side-list" style="top:775px">
    <li><svg width="14" height="14" viewBox="0 0 14 14"><circle cx="7" cy="7" r="6" fill="none" stroke="#555" stroke-width="1.3"/><path d="M5.5 4l3.5 3-3.5 3z" fill="#555"/></svg>Lorem Ipsum Posts...</li>
    <li><svg width="14" height="14" viewBox="0 0 14 14"><circle cx="7" cy="7" r="6" fill="none" stroke="#555" stroke-width="1.3"/><path d="M5.5 4l3.5 3-3.5 3z" fill="#555"/></svg>It is a long established fact...</li>
    <li><svg width="14" height="14" viewBox="0 0 14 14"><circle cx="7" cy="7" r="6" fill="none" stroke="#555" stroke-width="1.3"/><path d="M5.5 4l3.5 3-3.5 3z" fill="#555"/></svg>when an unknown printe...</li>
    <li><svg width="14" height="14" viewBox="0 0 14 14"><circle cx="7" cy="7" r="6" fill="none" stroke="#555" stroke-width="1.3"/><path d="M5.5 4l3.5 3-3.5 3z" fill="#555"/></svg>There are many variations of...</li>
    <li><svg width="14" height="14" viewBox="0 0 14 14"><circle cx="7" cy="7" r="6" fill="none" stroke="#555" stroke-width="1.3"/><path d="M5.5 4l3.5 3-3.5 3z" fill="#555"/></svg>comes from a line in...</li>
  </ul>

  <div class="abs side-head" style="top:911px">Archives</div>
  <ul class="abs side-list" style="top:955px">
    <li><svg width="14" height="14" viewBox="0 0 14 14"><circle cx="7" cy="7" r="6" fill="none" stroke="#555" stroke-width="1.3"/><path d="M5.5 4l3.5 3-3.5 3z" fill="#555"/></svg>January 2011</li>
    <li><svg width="14" height="14" viewBox="0 0 14 14"><circle cx="7" cy="7" r="6" fill="none" stroke="#555" stroke-width="1.3"/><path d="M5.5 4l3.5 3-3.5 3z" fill="#555"/></svg>February 2011</li>
    <li><svg width="14" height="14" viewBox="0 0 14 14"><circle cx="7" cy="7" r="6" fill="none" stroke="#555" stroke-width="1.3"/><path d="M5.5 4l3.5 3-3.5 3z" fill="#555"/></svg>March 2011</li>
    <li><svg width="14" height="14" viewBox="0 0 14 14"><circle cx="7" cy="7" r="6" fill="none" stroke="#555" stroke-width="1.3"/><path d="M5.5 4l3.5 3-3.5 3z" fill="#555"/></svg>April 2011</li>
    <li><svg width="14" height="14" viewBox="0 0 14 14"><circle cx="7" cy="7" r="6" fill="none" stroke="#555" stroke-width="1.3"/><path d="M5.5 4l3.5 3-3.5 3z" fill="#555"/></svg>May 2011</li>
  </ul>

  <aside class="abs ad" role="img" aria-label="Sidebar advertisement banner"></aside>

  <article class="abs post" style="top:380px">
    <h2>Neque porro quisquam est qui dolorem ipsum</h2>
    <div class="meta"><svg width="12" height="12" viewBox="0 0 12 12"><rect x="1" y="2" width="10" height="9" fill="#fff" stroke="#c44"/><rect x="1" y="2" width="10" height="3" fill="#c44"/></svg>11.05.11<span class="sep"></span><svg width="12" height="13" viewBox="0 0 12 13"><rect x="1" y="1" width="10" height="11" fill="#f4a640" stroke="#d67f10"/><path d="M3 4h6M3 6.5h6M3 9h6" stroke="#fff"/></svg>Serious Good Content<span class="sep"></span><svg width="12" height="13" viewBox="0 0 12 13"><circle cx="6" cy="4" r="3" fill="#444"/><path d="M1 12a5 5 0 0 1 10 0z" fill="#444"/></svg>Admin</div>
    <div class="thumb" role="img" aria-label="Photo of a group of friends gathered around a laptop" style="background:linear-gradient(120deg,#e8d0b8,#a8b4c8 50%,#d9c2a4)"></div>
    <p class="excerpt"><span>Lorem Ipsum is simply dummy text of the printing and typesetting indus-</span><span>try. Lorem Ipsum has been the industry's standard dummy text ever since</span><span>the 1500s, when an unknown printer took a galley an unknown printer</span><span>took a galley when an unknown prin &nbsp;Lorem Ipsum has been the indus-</span><span>try's stant...</span></p>
    <span class="more">Read More</span>
  </article>

  <article class="abs post" style="top:595px">
    <h2>Neque porro quisquam est qui dolorem ipsum</h2>
    <div class="meta"><svg width="12" height="12" viewBox="0 0 12 12"><rect x="1" y="2" width="10" height="9" fill="#fff" stroke="#c44"/><rect x="1" y="2" width="10" height="3" fill="#c44"/></svg>11.05.11<span class="sep"></span><svg width="12" height="13" viewBox="0 0 12 13"><rect x="1" y="1" width="10" height="11" fill="#f4a640" stroke="#d67f10"/><path d="M3 4h6M3 6.5h6M3 9h6" stroke="#fff"/></svg>Serious Good Content<span class="sep"></span><svg width="12" height="13" viewBox="0 0 12 13"><circle cx="6" cy="4" r="3" fill="#444"/><path d="M1 12a5 5 0 0 1 10 0z" fill="#444"/></svg>Admin</div>
    <div class="thumb" role="img" aria-label="Photo of a happy family outdoors" style="background:linear-gradient(120deg,#b8c860,#f0d8c0 45%,#f2e070)"></div>
    <p class="excerpt"><span>Lorem Ipsum is simply dummy text of the printing and typesetting indus-</span><span>try. Lorem Ipsum has been the industry's standard dummy text ever since</span><span>the 1500s, when an unknown printer took a galley an unknown printer</span><span>took a galley when an unknown prin &nbsp;Lorem Ipsum has been the indus-</span><span>try's stant...</span></p>
    <span class="more">Read More</span>
  </article>

  <article class="abs post" style="top:815px">
    <h2>Neque porro quisquam est qui dolorem ipsum</h2>
    <div class="meta"><svg width="12" height="12" viewBox="0 0 12 12"><rect x="1" y="2" width="10" height="9" fill="#fff" stroke="#c44"/><rect x="1" y="2" width="10" height="3" fill="#c44"/></svg>19.04.11<span class="sep"></span><svg width="12" height="13" viewBox="0 0 12 13"><rect x="1" y="1" width="10" height="11" fill="#f4a640" stroke="#d67f10"/><path d="M3 4h6M3 6.5h6M3 9h6" stroke="#fff"/></svg>Interior Design<span class="sep"></span><svg width="12" height="13" viewBox="0 0 12 13"><circle cx="6" cy="4" r="3" fill="#444"/><path d="M1 12a5 5 0 0 1 10 0z" fill="#444"/></svg>Admin</div>
    <div class="thumb" role="img" aria-label="Photo of a modern living room with a lounge chair and plant" style="background:linear-gradient(160deg,#ece8dc,#c8c2a8 50%,#5a4a38)"></div>
    <p class="excerpt"><span>Lorem Ipsum is simply dummy text of the printing and typesetting indus-</span><span>try. Lorem Ipsum has been the industry's standard dummy text ever since</span><span>the 1500s, when an unknown printer took a galley an unknown printer</span><span>took a galley when an unknown prin &nbsp;Lorem Ipsum has been the indus-</span><span>try's stant...</span></p>
    <span class="more">Read More</span>
  </article>

  <article class="abs post" style="top:1036px">
    <h2>Neque porro quisquam est qui dolorem ipsum</h2>
    <div class="meta"><svg width="12" height="12" viewBox="0 0 12 12"><rect x="1" y="2" width="10" height="9" fill="#fff" stroke="#c44"/><rect x="1" y="2" width="10" height="3" fill="#c44"/></svg>15.04.11<span class="sep"></span><svg width="12" height="13" viewBox="0 0 12 13"><rect x="1" y="1" width="10" height="11" fill="#f4a640" stroke="#d67f10"/><path d="M3 4h6M3 6.5h6M3 9h6" stroke="#fff"/></svg>Esteem Building<span class="sep"></span><svg width="12" height="13" viewBox="0 0 12 13"><circle cx="6" cy="4" r="3" fill="#444"/><path d="M1 12a5 5 0 0 1 10 0z" fill="#444"/></svg>Admin</div>
    <div class="thumb" role="img" aria-label="Photo of cheerful kids giving thumbs up under a blue sky" style="background:linear-gradient(170deg,#3f7fcf,#8ab8e8 40%,#e8a040 70%,#6a9a3a)"></div>
    <p class="excerpt"><span>Lorem Ipsum is simply dummy text of the printing and typesetting indus-</span><span>try. Lorem Ipsum has been the industry's standard dummy text ever since</span><span>the 1500s, when an unknown printer took a galley an unknown printer</span><span>took a galley when an unknown prin &nbsp;Lorem Ipsum has been the indus-</span><span>try's stant...</span></p>
    <span class="more">Read More</span>
  </article>

  <footer class="abs footer">Copyright @ 2011 by <b>ATTIC RESCUE BELLE</b></footer>
</div>
</body>
</html>
```